LUMEN BRIDGE WEBSITE

I need to get the design for the website of my company, which is a production company based in Los Angeles called LUMEN BRIDGE. The company works as a liason between Russian speaking and English speaking film communities, providing the spectrum of production services in Eastern Europe and United States of America.
Has to have the following links:
About
Locations
Works
I'd like to see the designs on the white background using the blue and red colors.
Please try to use the font of an old typewriter if you can. You can also get some ideas after looking at the logo, which you need to intergrate into the webdesign anyway.
Thank you very much and I wish you some inspiration!
Updates

I'd like to extend the project till July the 10th, please send more submissions

Reason: I want to give more time to make changes to my comments

Target Market(s)

Production studios from different countries, Directors, Producers, Clients

Industry/Entity Type

It Company

Font styles to use
Sans Serif
Other font styles liked:
• typewriter

Requirements
Must have
• Visible logo design intergrated into graphics

```html
<!DOCTYPE html>
<html lang="en">
<head>
<meta charset="utf-8">
<title>Lumen Bridge</title>
<link href="https://fonts.googleapis.com/css2?family=Special+Elite&family=Courier+Prime:wght@400;700&display=swap" rel="stylesheet">
<style>
  :root {
    --blue: #1e6aa1;
    --red: #c0272d;
    --ink: #1a1a1a;
    --grey-text: #555;
    --paper: #f4f4f4;
    --white: #ffffff;
  }
  * { box-sizing: border-box; margin: 0; padding: 0; }
  html, body { width: 1176px; height: 1200px; overflow: hidden; background: var(--white); }
  body { position: relative; font-family: "Courier Prime", "Courier New", monospace; color: var(--ink); }

  .top-bar { position: absolute; top: 0; left: 0; width: 1176px; height: 29px; background: var(--blue); }
  .social { position: absolute; right: 153px; top: 8px; display: flex; gap: 9px; }
  .social span { width: 13px; height: 13px; border-radius: 50%; background: var(--white); display: block; }

  .brand { position: absolute; left: 154px; top: 58px; display: flex; align-items: center; gap: 8px;
    font-family: "Special Elite", "Courier New", monospace; font-size: 26px; line-height: 30px; color: var(--blue); }
  .brand .mark { width: 14px; height: 14px; background: var(--red); }

  .main-nav { position: absolute; top: 56px; right: 153px; display: flex; }
  .main-nav a { font-family: "Special Elite", "Courier New", monospace; font-size: 16px; line-height: 20px; color: var(--ink); text-decoration: none; display: block; padding-top: 9px; }
  .main-nav a.about { width: 46px; color: var(--red); border-top: 2px solid var(--red); text-align: center; padding-top: 7px; margin-right: 79px; }
  .main-nav a.locations { width: 83px; text-align: left; }
  .main-nav a.works { width: 125px; text-align: right; }

  .hero { position: absolute; left: 154px; top: 119px; width: 869px; height: 412px; overflow: hidden; }
  .hero-art { position: absolute; inset: 0;
    background:
      linear-gradient(90deg, rgba(0,0,0,0) 0%, rgba(0,0,0,0) 55%, #140607 68%, #7a1419 82%, #b8232a 100%),
      radial-gradient(ellipse at 35% 45%, #a58a55 0%, #6e5530 45%, #2a1e10 85%); }
  .hero-shadow { position: absolute; left: 130px; top: 531px; width: 900px; height: 14px;
    background: radial-gradient(ellipse at 50% 0%, rgba(0,0,0,0.28), rgba(0,0,0,0) 70%); }
  .hero-copy { position: absolute; left: 63px; top: 138px; }
  .hero-copy h1 { font-family: "Special Elite", "Courier New", monospace; font-size: 34px; line-height: 40px; color: #111; letter-spacing: -1px; }
  .hero-copy p { margin-top: 4px; width: 480px; font-family: "Special Elite", "Courier New", monospace; font-size: 15.5px; line-height: 19px; color: #111; }
  .learn-more { position: absolute; left: 72px; top: 270px; width: 222px; height: 53px; border: 2px solid #1a140c;
    font-family: "Special Elite", "Courier New", monospace; font-size: 19px; color: var(--white); text-align: center; line-height: 49px; }
  .hero-arrow { position: absolute; top: 184px; width: 48px; height: 48px; border-radius: 50%; background: var(--white); }
  .hero-arrow.prev { left: -24px; }
  .hero-arrow.next { right: -24px; }
  .hero-arrow svg { position: absolute; top: 13px; }
  .hero-arrow.prev svg { left: 26px; }
  .hero-arrow.next svg { left: 14px; }

  .welcome { position: absolute; top: 576px; left: 0; width: 1176px; text-align: center; }
  .welcome h2 { display: inline-block; font-family: "Special Elite", "Courier New", monospace; font-weight: 400; font-size: 34px; line-height: 44px; color: var(--ink);
    padding: 0 2px 9px; border-bottom: 3px solid var(--blue); }
  .welcome h2 .name { color: var(--blue); }
  .welcome p { width: 750px; margin: 34px auto 0; font-size: 15px; line-height: 19.5px; letter-spacing: -0.4px; color: var(--grey-text); }

  .recent { position: absolute; top: 797px; left: 0; width: 1176px; height: 341px; background: var(--paper); }
  .recent h2 { position: absolute; top: 30px; width: 100%; text-align: center; font-family: "Special Elite", "Courier New", monospace; font-weight: 400; font-size: 42px; color: var(--ink); }
  .work-card { position: absolute; top: 123px; width: 244px; height: 146px; background: var(--white); border: 1px solid #e2e2e2; padding: 10px; }
  .work-card .thumb { width: 223px; height: 125px; position: relative; }
  .work-card .thumb svg { position: absolute; left: 80px; top: 31px; }
  .work-card::after { content: ""; position: absolute; left: 10px; right: 10px; bottom: -12px; height: 10px;
    background: radial-gradient(ellipse at 50% 0%, rgba(0,0,0,0.25), rgba(0,0,0,0) 70%); }
  .work-label { position: absolute; top: 286px; width: 244px; text-align: center; font-family: "Special Elite", "Courier New", monospace; font-size: 16px; color: var(--blue); }
  .card-1, .label-1 { left: 154px; }
  .card-2, .label-2 { left: 466px; }
  .card-3, .label-3 { left: 778px; }
  .thumb-doc { background: linear-gradient(180deg, #9a3b34 0%, #5f5a4a 55%, #6d6a63 100%); }
  .thumb-feature { background: linear-gradient(90deg, #2a0f08 0%, #8a4a35 45%, #3a1208 100%); }
  .thumb-music { background: linear-gradient(180deg, #121620 0%, #3d3f4a 60%, #2a2c33 100%); }
  .work-arrow { position: absolute; top: 168px; }
  .work-arrow.prev { left: 112px; }
  .work-arrow.next { right: 112px; }

  .site-footer { position: absolute; top: 1138px; left: 0; width: 1176px; height: 62px; background: var(--blue); color: var(--white); }
  .footer-nav { position: absolute; left: 154px; top: 22px; font-family: "Special Elite", "Courier New", monospace; font-size: 14px; }
  .footer-nav a { color: var(--white); text-decoration: none; }
  .footer-nav .sep { margin: 0 4px; }
  .copyright { position: absolute; right: 153px; top: 22px; font-family: "Special Elite", "Courier New", monospace; font-size: 14px; }
</style>
</head>
<body>
  <header>
    <div class="top-bar">
      <div class="social"><span></span><span></span><span></span><span></span><span></span><span></span></div>
    </div>
    <div class="brand"><span class="mark"></span>LUMEN BRIDGE</div>
    <nav class="main-nav">
      <a class="about" href="#">About</a>
      <a class="locations" href="#">Locations</a>
      <a class="works" href="#">Works</a>
    </nav>
  </header>

  <section class="hero">
    <div class="hero-art" role="img" aria-label="Worn film strip texture with a projector beam and a vintage movie camera on a tripod over a dark red gradient"></div>
    <div class="hero-copy">
      <h1>Place your tag line here</h1>
      <p>Lorem ipsum dolor sit amet, consectetur adipiscing elit. Aliquam vitae tellus dictum, dapibus orci blandit, lacinia lectus</p>
    </div>
    <div class="learn-more">Learn More</div>
    <div class="hero-arrow prev"><svg width="10" height="22" viewBox="0 0 10 22"><path d="M9 1 L1 11 L9 21" fill="none" stroke="#1e6aa1" stroke-width="1.6"/></svg></div>
    <div class="hero-arrow next"><svg width="10" height="22" viewBox="0 0 10 22"><path d="M1 1 L9 11 L1 21" fill="none" stroke="#1e6aa1" stroke-width="1.6"/></svg></div>
  </section>
  <div class="hero-shadow"></div>

  <section class="welcome">
    <h2>Welcome to <span class="name">LUMEN BRIDGE</span></h2>
    <p>Lorem ipsum dolor sit amet, consectetur adipiscing elit. Aliquam vitae tellus dictum, dapibus orci blandit, lacinia lectus. Praesent at nunc arcu. Nam viverra nisl sit amet felis porttitor ultrices. Cum sociis natoque penatibus et magnis dis parturient montes, nascetur ridiculus mus. Donec iaculis adipiscing.</p>
  </section>

  <section class="recent">
    <h2>Our Recent Work</h2>
    <svg class="work-arrow prev" width="20" height="56" viewBox="0 0 20 56"><path d="M18 1 L2 28 L18 55" fill="none" stroke="#333" stroke-width="2"/></svg>
    <svg class="work-arrow next" width="20" height="56" viewBox="0 0 20 56"><path d="M2 1 L18 28 L2 55" fill="none" stroke="#333" stroke-width="2"/></svg>

    <div class="work-card card-1"><div class="thumb thumb-doc" role="img" aria-label="Documentary still of a military parade">
      <svg width="62" height="62" viewBox="0 0 62 62"><circle cx="31" cy="31" r="28" fill="rgba(255,255,255,0.15)" stroke="#ddd" stroke-width="4"/><path d="M25 19 L43 31 L25 43 Z" fill="#ddd"/></svg></div></div>
    <div class="work-card card-2"><div class="thumb thumb-feature" role="img" aria-label="Feature film still in warm dark tones">
      <svg width="62" height="62" viewBox="0 0 62 62"><circle cx="31" cy="31" r="28" fill="rgba(255,255,255,0.15)" stroke="#ddd" stroke-width="4"/><path d="M25 19 L43 31 L25 43 Z" fill="#ddd"/></svg></div></div>
    <div class="work-card card-3"><div class="thumb thumb-music" role="img" aria-label="Music video still of a band on stage">
      <svg width="62" height="62" viewBox="0 0 62 62"><circle cx="31" cy="31" r="28" fill="rgba(255,255,255,0.15)" stroke="#ddd" stroke-width="4"/><path d="M25 19 L43 31 L25 43 Z" fill="#ddd"/></svg></div></div>

    <div class="work-label label-1">Documentary</div>
    <div class="work-label label-2">Feature Film</div>
    <div class="work-label label-3">Music</div>
  </section>

  <footer class="site-footer">
    <nav class="footer-nav">
      <a href="#">Home</a><span class="sep">|</span><a href="#">About</a><span class="sep">|</span><a href="#">Locations</a><span class="sep">|</span><a href="#">Works</a><span class="sep">|</span><a href="#">Conatct us</a>
    </nav>
    <div class="copyright">Copyright © 2014 Lumen Bridge</div>
  </footer>
</body>
</html>
```